International Honeymoon Tour Operator needs Business Card

We need to design a business card including our new logo for a new tour operator called Marisol Fenwick Holidays. We would like to also include the text 'Personal Tailor-Made Honeymoons for our Guests at a Lower Cost'. Please Include the following details as well; 'Website: www.marisolfenwickholidays.co.uk'; 'E-mail: tobias@marisolfenwickholidays.co.uk'; 'Mobile: 07914266058'. We would like the design to be compatible with the logo and text. The final design should communicate professionalism, modern and ethical.

We want to business card to be double sided.

We would like to be able to easily adjust the e-mail address and contact number in the future for other employees either through you or ourselves.

Target Market(s)

Brides and grooms aged 18-35 predominantly.

Industry/Entity Type

Business

Colors

Designer to choose colors to be used in the design.

Requirements
Must have
• Logo
Requested Text
Double sided
Nice to have
• Additional colour
The wow factor
Should not have
• Images of currency

```html
<!DOCTYPE html>
<html lang="en">
<head>
<meta charset="utf-8">
<title>Marisol Fenwick Holidays – Business Card</title>
<link href="https://fonts.googleapis.com/css2?family=Signika:wght@300;400&family=Arimo:wght@400&display=swap" rel="stylesheet">
<style>
  :root {
    --backdrop: #e6e4df;
    --card: #ffffff;
    --lime: #8dc63f;
    --lime-soft: #a9d46a;
    --teal: #3d6b5e;
    --ink: #1f1f1f;
    --watermark: #ebece8;
  }
  * { margin: 0; padding: 0; box-sizing: border-box; }
  html, body { width: 1200px; height: 873px; overflow: hidden; }
  body {
    background: var(--backdrop);
    display: flex;
    align-items: center;
    justify-content: center;
    gap: 60px;
    font-family: "Signika", sans-serif;
  }
  .card {
    position: relative;
    width: 520px;
    height: 297px;
    background: var(--card);
    overflow: hidden;
    box-shadow: 0 2px 10px rgba(0,0,0,0.12);
  }

  /* Back side: contact details */
  .card-back .band {
    position: absolute;
    left: 0; right: 0; bottom: 0;
    height: 22px;
    background: var(--lime);
  }
  .card-back .watermark-name {
    position: absolute;
    right: 30px;
    top: 62px;
    width: 300px;
    text-align: right;
    font-family: "Signika", sans-serif;
    font-weight: 300;
    font-size: 52px;
    line-height: 1;
    color: var(--watermark);
  }
  .card-back .contact {
    position: absolute;
    left: 28px;
    bottom: 36px;
    list-style: none;
    font-family: "Arimo", sans-serif;
    font-size: 19px;
    line-height: 1.22;
    color: var(--ink);
  }

  /* Front side: brand and tagline */
  .card-front .wave {
    position: absolute;
    inset: 0;
    width: 100%;
    height: 100%;
  }
  .card-front .brand {
    position: absolute;
    right: 40px;
    top: 44px;
    display: flex;
    align-items: center;
    gap: 14px;
  }
  .card-front .brand-mark {
    width: 30px;
    height: 30px;
    border-radius: 50%;
    background: var(--teal);
    flex: none;
  }
  .card-front .brand-name {
    font-family: "Signika", sans-serif;
    font-weight: 300;
    font-size: 38px;
    line-height: 1.02;
    color: var(--teal);
  }
  .card-front .tagline {
    position: absolute;
    left: 20px;
    top: 14px;
    width: 300px;
    font-family: "Signika", sans-serif;
    font-weight: 400;
    font-size: 14px;
    line-height: 1.3;
    color: #1e2a14;
  }
</style>
</head>
<body>

  <section class="card card-back" aria-label="Business card, back">
    <div class="watermark-name">Marisol<br>Fenwick</div>
    <ul class="contact">
      <li>Cell: 07914266058</li>
      <li>tobias@marisolfenwickholidays.co.uk</li>
      <li>www.marisolfenwickholidays.co.uk</li>
    </ul>
    <div class="band"></div>
  </section>

  <section class="card card-front" aria-label="Business card, front">
    <svg class="wave" viewBox="0 0 520 297" preserveAspectRatio="none" aria-hidden="true">
      <path d="M0 0 H260 C230 60 260 120 330 170 C390 212 440 250 470 297 H0 Z" fill="var(--lime)"/>
      <path d="M120 0 C110 80 200 170 300 220 C360 250 400 270 430 297" fill="none" stroke="#ffffff" stroke-opacity="0.7" stroke-width="1.2"/>
    </svg>
    <p class="tagline">Personal Tailor-Made Honeymoons for our guests at a lower costs</p>
    <div class="brand">
      <span class="brand-mark"></span>
      <span class="brand-name">Marisol Fenwick<br>Holidays</span>
    </div>
  </section>

</body>
</html>
```